Corroway Medical Imaging marketing poster

A poster to advertise our services. Something outstanding that catches the eye. Will be displayed at medical centres. Needs to advertise the following:
Opening hours - Mon-fri 8am-5:30pm Sat 8am-12:30
Services offered: Ultrasound, CT, Xray, Conebeam CT, Barium Studies, Injections and Biopsies, 3D/4D pregnancy scans.
We Bulk Bill concession card holders and under 18's
Locally owned and operated
www.corrowaymedicalimaging.example.au
include contact details also Tel: 96384027 Fax: 9638 4093

```html
<!DOCTYPE html>
<html lang="en">
<head>
<meta charset="utf-8">
<title>Corroway Medical Imaging – Services Poster</title>
<link rel="stylesheet" href="https://fonts.googleapis.com/css2?family=Open+Sans:wght@400;600;700&family=Roboto+Condensed:wght@300;400;700&display=swap">
<style>
  :root {
    --blue-deep: #1a4f86;
    --blue-mid: #2566a5;
    --blue-light: #3a86c6;
    --bubble-blue: #2a70b0;
    --lime: #9ccc1c;
    --lime-text: #c4e635;
    --navy: #1d3f73;
    --photo-light: #eef1f3;
    --photo-mid: #cfd6dc;
    --white: #ffffff;
    --footer-text: #1e2a35;
  }
  html, body {
    margin: 0;
    padding: 0;
    width: 849px;
    height: 1200px;
    overflow: hidden;
    background: var(--white);
  }
  .poster {
    position: relative;
    width: 849px;
    height: 1200px;
    overflow: hidden;
  }
  .poster-art {
    position: absolute;
    inset: 0;
    display: block;
  }
  .hours-title { font: 700 31px "Open Sans", sans-serif; fill: var(--white); }
  .hours-line { font: 700 21px "Open Sans", sans-serif; fill: var(--lime-text); }
  .services-heading { font: 600 19px "Open Sans", sans-serif; fill: var(--lime-text); letter-spacing: 0.3px; }
  .service-item { font: 400 23px "Open Sans", sans-serif; fill: var(--white); }
  .headline { fill: var(--white); font-family: "Roboto Condensed", sans-serif; }
  .headline-regular { font-weight: 400; }
  .headline-light { font-weight: 300; }
  .headline-bold { font-weight: 700; }
  .brand-name { font: 600 27px "Open Sans", sans-serif; fill: var(--navy); letter-spacing: 1px; }
  .brand-sub { font: 600 15px "Open Sans", sans-serif; fill: var(--navy); letter-spacing: 1.5px; }
  .footer-text { font: 400 16px "Open Sans", sans-serif; fill: var(--footer-text); }
</style>
</head>
<body>
<main class="poster">
  <svg class="poster-art" viewBox="0 0 849 1200" width="849" height="1200" xmlns="http://www.w3.org/2000/svg">
    <defs>
      <linearGradient id="bg-blue" x1="0" y1="0" x2="0.4" y2="1">
        <stop offset="0" stop-color="var(--blue-light)"/>
        <stop offset="0.5" stop-color="var(--blue-mid)"/>
        <stop offset="1" stop-color="var(--blue-deep)"/>
      </linearGradient>
      <linearGradient id="photo-tone" x1="0" y1="0" x2="1" y2="1">
        <stop offset="0" stop-color="var(--photo-light)"/>
        <stop offset="1" stop-color="var(--photo-mid)"/>
      </linearGradient>
      <radialGradient id="bubble-fill" cx="0.5" cy="0.45" r="0.6">
        <stop offset="0" stop-color="var(--blue-light)"/>
        <stop offset="1" stop-color="var(--bubble-blue)"/>
      </radialGradient>
    </defs>

    <!-- blue backdrop -->
    <rect class="backdrop" x="0" y="0" width="849" height="1200" fill="url(#bg-blue)"/>

    <!-- lime swoosh band -->
    <path class="swoosh-band" fill="var(--lime)"
      d="M0,500 C160,478 320,500 455,560 L560,440 C650,345 760,270 849,160 L849,225 C770,310 680,375 600,450 L462,585 C320,530 160,515 0,535 Z"/>

    <!-- photo area -->
    <g class="hero-photo" role="img" aria-label="Sonographer seated at an ultrasound machine in a bright clinic room">
      <path fill="url(#photo-tone)"
        d="M0,0 H849 V160 C760,270 650,345 560,440 L455,560 C320,500 160,478 0,500 Z"/>
    </g>

    <!-- opening hours bubble -->
    <g class="hours-bubble">
      <path fill="var(--bubble-blue)" d="M450,562 L520,520 L540,585 Z"/>
      <circle cx="612" cy="536" r="110" fill="url(#bubble-fill)"/>
      <path fill="none" stroke="var(--lime)" stroke-width="9" stroke-linecap="round"
        d="M560,440 A112,112 0 0 0 600,648"/>
      <path fill="none" stroke="var(--bubble-blue)" stroke-width="5" stroke-linecap="round"
        d="M572,455 A96,96 0 0 0 598,630"/>
      <text class="hours-title" x="532" y="499">Opening hours -</text>
      <text class="hours-line" x="532" y="531">Mon-fri 8am-5:30pm</text>
      <text class="hours-line" x="532" y="559">Sat 8am-12:30</text>
    </g>

    <!-- brand -->
    <g class="brand">
      <circle cx="44" cy="50" r="26" fill="var(--lime)"/>
      <text class="brand-name" x="80" y="52">CORROWAY</text>
      <text class="brand-sub" x="81" y="75">MEDICAL IMAGING</text>
    </g>

    <!-- services list -->
    <g class="services">
      <text class="services-heading" x="43" y="673">SERVICES OFFERED:</text>
      <line x1="44" y1="722" x2="44" y2="1098" stroke="var(--white)" stroke-opacity="0.35" stroke-width="1"/>
      <g fill="var(--white)">
        <circle cx="44" cy="726" r="3.5"/>
        <circle cx="44" cy="788" r="3.5"/>
        <circle cx="44" cy="850" r="3.5"/>
        <circle cx="44" cy="913" r="3.5"/>
        <circle cx="44" cy="973" r="3.5"/>
        <circle cx="44" cy="1035" r="3.5"/>
        <circle cx="44" cy="1096" r="3.5"/>
      </g>
      <text class="service-item" x="76" y="733">Ultrasound</text>
      <text class="service-item" x="76" y="795">CT</text>
      <text class="service-item" x="76" y="857">Xray</text>
      <text class="service-item" x="76" y="920">Conebeam CT</text>
      <text class="service-item" x="76" y="980">Barium Studies</text>
      <text class="service-item" x="76" y="1042">Injections and Biopsies</text>
      <text class="service-item" x="76" y="1103">3D/4D pregnancy scans</text>
    </g>

    <!-- headline -->
    <g class="headline">
      <text class="headline-regular" x="434" y="730" font-size="92" textLength="370" lengthAdjust="spacingAndGlyphs">WE BULK</text>
      <text class="headline-bold" x="434" y="795" font-size="50" textLength="366" lengthAdjust="spacingAndGlyphs">BILL CONCESSION</text>
      <text class="headline-light" x="434" y="856" font-size="50" textLength="366" lengthAdjust="spacingAndGlyphs">CARD HOLDERS AND</text>
      <text class="headline-bold" x="434" y="941" font-size="82" textLength="366" lengthAdjust="spacingAndGlyphs">UNDER 18'S</text>
      <text class="headline-light" x="434" y="998" font-size="50" textLength="366" lengthAdjust="spacingAndGlyphs">LOCALLY OWNED AND</text>
      <text class="headline-bold" x="434" y="1101" font-size="108" textLength="366" lengthAdjust="spacingAndGlyphs">OPERATED</text>
    </g>

    <!-- footer -->
    <g class="footer">
      <rect x="0" y="1148" width="849" height="52" fill="var(--lime)"/>
      <text class="footer-text" x="48" y="1180">www.corrowaymedicalimaging.example.au</text>
      <text class="footer-text" x="833" y="1180" text-anchor="end">Tel: 96384027 Fax: 9638 4093</text>
    </g>
  </svg>
</main>
</body>
</html>
```